Website Design for a holiday home letting busines

We require a redesign of our present website www.birchwoodstays.com. We want the website to stand out and look professional and clean to make holiday hunters want to book a caravan or lodge holiday with us. Our logo is red however we DO NOT want the website to be red. We want a natural colour scheme.

The final design should communicate that we are a professional company to book with.

On the home page we require;
Overview of company
Photo
Search box for holiday (check in)
Late Deals
Reviews
News

We would like the following pages designed; home page, available dates page, caravans page, content page.

The website should be responsive for smart phones. One website I do like is http://www.verdamoro.be/nl/

Target Market(s)

Families

Industry/Entity Type

Travel

Number of Pages Required

5+ page

Font styles to use
Serif

Requirements
Must have
• The project must be responsive for mobile phones and tablets.
• Ability to search for holiday home holidays
• We want a natural colour scheme.
Nice to have
• A style we like is http://www.verdamoro.be/nl/
Should not have
• Do not use red as a colour for the website. Our logo is red so this is the only time we want this used.

```html
<!DOCTYPE html>
<html lang="en">
<head>
<meta charset="utf-8">
<title>Birchwood Stays – Private Holiday Rentals</title>
<link rel="stylesheet" href="https://fonts.googleapis.com/css2?family=Open+Sans:wght@400;600;700;800&display=swap">
<style>
:root{
  --blue:#3d85c6;
  --blue-dark:#2f6ea8;
  --navy:#2c3a48;
  --navy-deep:#222e3a;
  --footer:#26323e;
  --footer-bottom:#1e2831;
  --ink:#3a3f45;
  --muted:#8a9198;
  --line:#e3e6e9;
  --paper:#ffffff;
  --soft:#f4f6f8;
  --star:#f2b630;
}
*{box-sizing:border-box;margin:0;padding:0}
html,body{width:1200px;height:2576px;overflow:hidden}
body{font-family:"Open Sans",Arial,sans-serif;color:var(--ink);background:var(--paper);font-size:13px;line-height:1.55}
.page{position:relative;width:1200px;height:2576px}

/* header */
.site-header{height:96px;display:flex;align-items:center;justify-content:space-between;padding:0 160px}
.brand{display:flex;align-items:center;gap:10px}
.brand-dot{width:36px;height:36px;border-radius:50%;background:var(--navy)}
.brand-name{font-size:24px;font-weight:700;color:var(--navy)}
.brand-tag{font-size:10px;color:var(--muted);margin-top:-4px}
.header-contact{display:flex;align-items:center;gap:22px;font-size:12px;color:var(--muted)}
.header-contact span{display:flex;align-items:center;gap:6px}
.social-square{width:22px;height:22px;background:var(--blue-dark);border-radius:3px}

.main-nav{height:36px;background:var(--blue);margin:0 160px;display:flex;align-items:center}
.main-nav a{color:#fff;text-decoration:none;font-size:10px;font-weight:600;text-transform:uppercase;padding:0 14px;height:36px;line-height:36px}
.main-nav a.active{background:var(--blue-dark)}
.main-nav a:last-child{margin-left:auto}

/* hero */
.hero{position:relative;height:548px;margin-top:0}
.hero-photo{position:absolute;inset:0;background:linear-gradient(180deg,#8fc0e6 0%,#c6e0f3 40%,#6fb4d6 48%,#a9d6e6 58%,#efe7d6 66%,#f7f2e8 100%)}
.hero-copy{position:absolute;left:160px;top:170px;color:#fff}
.hero-copy .eyebrow{font-size:26px;font-weight:800;letter-spacing:1px}
.hero-copy h1{font-size:58px;font-weight:800;line-height:1;letter-spacing:1px}
.hero-copy p{font-size:11px;font-weight:600;width:300px;margin-top:14px;text-transform:uppercase}
.book-badge{position:absolute;right:170px;top:0;width:78px;height:74px;background:var(--blue);color:#fff;font-size:12px;font-weight:700;text-align:center;padding-top:18px;line-height:1.3}
.hero-arrow{position:absolute;top:250px;width:36px;height:36px;border-radius:50%;background:rgba(255,255,255,.85);display:flex;align-items:center;justify-content:center}
.hero-arrow.left{left:20px}.hero-arrow.right{right:20px}

/* search */
.search-bar{height:64px;background:var(--soft);border-bottom:1px solid var(--line);display:flex;align-items:center;padding:0 160px;gap:12px}
.search-label{font-size:10px;color:var(--muted);line-height:1.2;width:150px}
.search-label b{display:block;font-size:15px;color:var(--navy);font-weight:700}
.field{height:30px;border:1px solid #d5d9dd;background:#fff;font-size:11px;color:var(--muted);display:flex;align-items:center;padding:0 10px}
.btn{background:var(--blue);color:#fff;font-size:10px;font-weight:700;text-transform:uppercase;display:inline-flex;align-items:center;justify-content:center}
.search-bar .btn{height:30px;padding:0 18px}

/* section titles */
.section-title{text-align:center;font-size:20px;font-weight:700;color:var(--navy);text-transform:uppercase}
.section-lead{text-align:center;font-size:11px;color:var(--muted);width:520px;margin:6px auto 0}

/* late deals */
.late-deals{position:relative;height:370px;padding-top:36px}
.card-row{display:flex;gap:20px;justify-content:center;margin-top:24px}
.deal-card{width:202px;border:1px solid var(--line);background:#fff}
.deal-photo{height:112px;position:relative}
.price-tag{position:absolute;right:-6px;top:-6px;width:34px;height:34px;border-radius:50%;background:var(--blue);color:#fff;font-size:10px;font-weight:700;display:flex;align-items:center;justify-content:center}
.deal-body{padding:10px 12px;font-size:10px;color:var(--muted)}
.deal-body h3{font-size:11px;color:var(--ink);font-weight:600}
.deal-foot{display:flex;justify-content:space-between;align-items:center;margin-top:6px}
.deal-foot .btn{height:20px;padding:0 10px;font-size:9px}
.row-arrow{position:absolute;top:250px;width:28px;height:28px;border-radius:50%;border:1px solid #cfd4d9;display:flex;align-items:center;justify-content:center;background:#fff}
.row-arrow.left{left:80px}.row-arrow.right{right:80px}

/* overview */
.overview{height:310px;border-top:1px solid var(--line);display:flex;gap:40px;padding:36px 160px 0}
.overview-main{flex:1}
.col-title{font-size:17px;font-weight:700;color:var(--navy);text-transform:uppercase;border-bottom:1px solid var(--line);padding-bottom:8px;margin-bottom:14px}
.overview-body{display:flex;gap:18px}
.overview-photo{width:230px;height:170px;flex:none;background:linear-gradient(135deg,#c9b79a,#8f7d62)}
.overview-text p{font-size:11px;color:var(--muted);margin-bottom:8px}
.overview-text .highlight{color:var(--blue);font-weight:600}
.reviews{width:280px}
.review{margin-bottom:14px;font-size:11px;color:var(--muted)}
.review .quote{color:var(--blue)}
.stars{color:var(--star);font-size:12px;letter-spacing:1px}

/* caravans */
.caravans{position:relative;height:500px;background:linear-gradient(180deg,var(--navy) 0%,var(--navy-deep) 100%);padding-top:44px}
.caravans .section-title{color:#fff}
.caravans .section-lead{color:#aab4be}
.caravans .deal-card{border:none}
.caravans .deal-photo{height:150px}
.caravans .row-arrow{top:260px;background:transparent;border-color:#7c8893}

/* blog */
.blog{height:350px;display:flex;gap:40px;padding:40px 160px 0;position:relative}
.blog-main{flex:1}
.blog-row{display:flex;gap:18px}
.post{width:158px}
.post-photo{height:110px;position:relative}
.post-date{position:absolute;left:0;bottom:0;background:var(--blue);color:#fff;font-size:9px;font-weight:700;padding:2px 8px}
.post h4{font-size:11px;color:var(--blue);font-weight:600;margin-top:8px}
.post p{font-size:10px;color:var(--muted)}
.feed{width:280px}
.feed-item{display:flex;gap:10px;margin-bottom:14px}
.feed-photo{width:60px;height:50px;flex:none}
.feed-item p{font-size:10px;color:var(--muted)}
.feed-item b{color:var(--blue);font-weight:600;font-size:11px;display:block}
.live-chat{position:absolute;right:150px;bottom:18px;background:var(--blue);color:#fff;font-size:11px;font-weight:700;padding:6px 16px;border-radius:3px 3px 0 0}

/* footer */
.site-footer{height:282px;background:var(--footer);padding:34px 160px 0;display:flex;gap:40px;color:#aab4be;font-size:10px}
.foot-col{flex:1}
.foot-col h5{color:#fff;font-size:11px;font-weight:700;text-transform:uppercase;margin-bottom:14px}
.foot-col li{list-style:none;margin-bottom:7px;display:flex;gap:6px;align-items:flex-start}
.foot-col .field{background:#334250;border-color:#3d4c5a;height:24px;margin-bottom:8px;color:#8e9aa6;font-size:10px}
.foot-col .btn{height:24px;padding:0 14px}
.links{display:flex;gap:30px}
.footer-bottom{height:50px;background:var(--footer-bottom);display:flex;align-items:center;justify-content:space-between;padding:0 160px;color:#7f8b97;font-size:10px}
.socials{display:flex;gap:6px}
.socials i{width:20px;height:20px;border-radius:50%;border:1px solid #5b6875;display:block}
</style>
</head>
<body>
<div class="page">

<header class="site-header">
  <div class="brand">
    <div class="brand-dot"></div>
    <div>
      <div class="brand-name">Birchwood Stays</div>
      <div class="brand-tag">Caravan &amp; lodge holidays</div>
    </div>
  </div>
  <div class="header-contact">
    <span><svg width="12" height="10" viewBox="0 0 12 10"><rect x="0.5" y="0.5" width="11" height="9" fill="none" stroke="#8a9198"/><path d="M0.5 0.5L6 5.5L11.5 0.5" fill="none" stroke="#8a9198"/></svg>info@birchwoodstays.com</span>
    <span><svg width="11" height="11" viewBox="0 0 12 12"><path d="M2 1l2.5 0 1 3-1.5 1a7 7 0 0 0 3 3l1-1.5 3 1V10a1.5 1.5 0 0 1-1.5 1.5C4.5 11.5.5 7.5.5 2.5A1.5 1.5 0 0 1 2 1z" fill="#8a9198"/></svg>01632 960 418</span>
    <div class="social-square"></div>
  </div>
</header>

<nav class="main-nav">
  <a class="active" href="#">Home</a><a href="#">About</a><a href="#">Reviews</a><a href="#">Caravans &amp; Lodges</a><a href="#">Gallery</a><a href="#">Late Deals</a><a href="#">Holiday Parks</a><a href="#">Local Attractions</a><a href="#">Contact Us</a>
</nav>

<section class="hero">
  <div class="hero-photo" role="img" aria-label="Sunny beach with two deck chairs under a yellow parasol by a turquoise sea"></div>
  <div class="book-badge">BOOK<br>NOW</div>
  <div class="hero-copy">
    <div class="eyebrow">PRIVATE</div>
    <h1>HOLIDAY<br>RENTALS</h1>
    <p>Quality lodges and caravans in peaceful countryside and coastal parks across the region</p>
  </div>
  <div class="hero-arrow left"><svg width="10" height="12" viewBox="0 0 10 12"><path d="M7 1L2 6l5 5" stroke="#2c3a48" stroke-width="2" fill="none"/></svg></div>
  <div class="hero-arrow right"><svg width="10" height="12" viewBox="0 0 10 12"><path d="M3 1l5 5-5 5" stroke="#2c3a48" stroke-width="2" fill="none"/></svg></div>
</section>

<section class="search-bar">
  <div class="search-label">SEARCH BOX<b>FOR HOLIDAY</b></div>
  <div class="field" style="width:90px">Check in date</div>
  <div class="field" style="width:150px">dd/mm/yyyy</div>
  <div class="field" style="width:140px">Night of Nights ▾</div>
  <div class="field" style="width:150px">Any</div>
  <div class="btn">Search Now</div>
</section>

<section class="late-deals">
  <h2 class="section-title">Late Deals</h2>
  <p class="section-lead">Grab a last minute break at one of our lodges or caravans with a reduced nightly price while dates remain.</p>
  <div class="row-arrow left"><svg width="8" height="10" viewBox="0 0 8 10"><path d="M6 1L2 5l4 4" stroke="#8a9198" stroke-width="1.5" fill="none"/></svg></div>
  <div class="row-arrow right"><svg width="8" height="10" viewBox="0 0 8 10"><path d="M2 1l4 4-4 4" stroke="#8a9198" stroke-width="1.5" fill="none"/></svg></div>
  <div class="card-row">
    <article class="deal-card"><div class="deal-photo" role="img" aria-label="Bright lodge bedroom" style="background:linear-gradient(135deg,#d9c3a0,#8a6d4e)"><span class="price-tag">£99</span></div><div class="deal-body"><h3>The Details</h3>Friday 14 September 2013<div class="deal-foot">Nights 3<span class="btn">Book Now</span></div></div></article>
    <article class="deal-card"><div class="deal-photo" role="img" aria-label="Cosy caravan living room" style="background:linear-gradient(135deg,#c89a6a,#6e4b33)"><span class="price-tag">£99</span></div><div class="deal-body"><h3>The Details</h3>Friday 14 September 2013<div class="deal-foot">Nights 3<span class="btn">Book Now</span></div></div></article>
    <article class="deal-card"><div class="deal-photo" role="img" aria-label="Lodge double bedroom" style="background:linear-gradient(135deg,#b9a58c,#5d5144)"><span class="price-tag">£99</span></div><div class="deal-body"><h3>The Details</h3>Friday 14 September 2013<div class="deal-foot">Nights 3<span class="btn">Book Now</span></div></div></article>
    <article class="deal-card"><div class="deal-photo" role="img" aria-label="Park swimming pool by the lodges" style="background:linear-gradient(135deg,#8fd0e6,#3a93b8)"><span class="price-tag">£99</span></div><div class="deal-body"><h3>The Details</h3>Friday 14 September 2013<div class="deal-foot">Nights 3<span class="btn">Book Now</span></div></div></article>
  </div>
</section>

<section class="overview">
  <div class="overview-main">
    <h2 class="col-title">Overview of Company</h2>
    <div class="overview-body">
      <div class="overview-photo" role="img" aria-label="Lodge interior with sofa and dining area"></div>
      <div class="overview-text">
        <p class="highlight">We are a family run business letting holiday lodges and caravans on quiet parks.</p>
        <p>Birchwood Stays has welcomed families for many years, offering homes in carefully chosen locations close to the coast and the countryside.</p>
        <p>Every property is cleaned, checked and equipped for a relaxing stay, so you can simply arrive, unpack and enjoy time together. Book online in minutes or call our friendly team for help choosing the right home.</p>
      </div>
    </div>
  </div>
  <aside class="reviews">
    <h2 class="col-title">Latest Reviews</h2>
    <div class="review"><span class="quote">Lovely clean lodge and a warm welcome.</span> The children loved the park and we will be back next year.<div class="stars">★★★★★</div></div>
    <div class="review"><span class="quote">Great value late deal for our family.</span> Spacious caravan with everything we needed for the week.<div class="stars">★★★★★</div></div>
  </aside>
</section>

<section class="caravans">
  <h2 class="section-title">List of Caravans and Lodges</h2>
  <p class="section-lead">Browse our full range of holiday homes, from compact caravans to spacious family lodges with hot tubs.</p>
  <div class="row-arrow left"><svg width="8" height="10" viewBox="0 0 8 10"><path d="M6 1L2 5l4 4" stroke="#c9d1d8" stroke-width="1.5" fill="none"/></svg></div>
  <div class="row-arrow right"><svg width="8" height="10" viewBox="0 0 8 10"><path d="M2 1l4 4-4 4" stroke="#c9d1d8" stroke-width="1.5" fill="none"/></svg></div>
  <div class="card-row" style="margin-top:34px">
    <article class="deal-card"><div class="deal-photo" role="img" aria-label="Lodge bedroom with wooden furniture" style="background:linear-gradient(135deg,#cdb391,#7b6045)"></div><div class="deal-body"><h3>The Details</h3>Friday 14 September 2013<div class="deal-foot">Nights 3</div><div style="margin-top:8px"><span class="btn" style="height:22px;padding:0 12px">Read More</span></div></div></article>
    <article class="deal-card"><div class="deal-photo" role="img" aria-label="Caravan lounge with sofa" style="background:linear-gradient(135deg,#e1d3bd,#9c8466)"></div><div class="deal-body"><h3>The Details</h3>Friday 14 September 2013<div class="deal-foot">Nights 3</div><div style="margin-top:8px"><span class="btn" style="height:22px;padding:0 12px">Read More</span></div></div></article>
    <article class="deal-card"><div class="deal-photo" role="img" aria-label="Lodge twin bedroom" style="background:linear-gradient(135deg,#bfae98,#60554a)"></div><div class="deal-body"><h3>The Details</h3>Friday 14 September 2013<div class="deal-foot">Nights 3</div><div style="margin-top:8px"><span class="btn" style="height:22px;padding:0 12px">Read More</span></div></div></article>
    <article class="deal-card"><div class="deal-photo" role="img" aria-label="Lodge exterior lit at dusk" style="background:linear-gradient(135deg,#4c5d7a,#c79a5f)"></div><div class="deal-body"><h3>The Details</h3>Friday 14 September 2013<div class="deal-foot">Nights 3</div><div style="margin-top:8px"><span class="btn" style="height:22px;padding:0 12px">Read More</span></div></div></article>
  </div>
</section>

<section class="blog">
  <div class="blog-main">
    <h2 class="col-title">Latest Blog News</h2>
    <div class="blog-row">
      <article class="post"><div class="post-photo" role="img" aria-label="Lodge bedroom" style="background:linear-gradient(135deg,#d2b48c,#7d5f40)"><span class="post-date">August 15, 2013</span></div><h4>New lodges open this season</h4><p>Three new family lodges are now ready to book for spring breaks.</p></article>
      <article class="post"><div class="post-photo" role="img" aria-label="Caravan interior" style="background:linear-gradient(135deg,#c4ab8c,#6f5a44)"><span class="post-date">August 15, 2013</span></div><h4>Top days out nearby</h4><p>Our guide to beaches, walks and attractions close to the parks.</p></article>
      <article class="post"><div class="post-photo" role="img" aria-label="Lodge kitchen" style="background:linear-gradient(135deg,#dccab2,#8d7862)"><span class="post-date">August 15, 2013</span></div><h4>Pet friendly breaks</h4><p>Bring the whole family, dogs included, to selected homes.</p></article>
    </div>
  </div>
  <aside class="feed">
    <h2 class="col-title">Social Feed</h2>
    <div class="feed-item"><div class="feed-photo" role="img" aria-label="Lodge bedroom" style="background:linear-gradient(135deg,#d4b996,#7a5e43)"></div><p><b>Autumn dates now live</b>Book early to secure the best homes for half term.</p></div>
    <div class="feed-item"><div class="feed-photo" role="img" aria-label="Lodge living area" style="background:linear-gradient(135deg,#c7b197,#6c5945)"></div><p><b>Guest photo of the week</b>A sunny morning on the lodge decking.</p></div>
  </aside>
  <div class="live-chat">LIVE CHAT</div>
</section>

<footer class="site-footer">
  <div class="foot-col">
    <h5>Contact Us</h5>
    <ul>
      <li><svg width="10" height="10" viewBox="0 0 12 12"><path d="M2 1l2.5 0 1 3-1.5 1a7 7 0 0 0 3 3l1-1.5 3 1V10a1.5 1.5 0 0 1-1.5 1.5C4.5 11.5.5 7.5.5 2.5A1.5 1.5 0 0 1 2 1z" fill="#aab4be"/></svg>01632 960 418</li>
      <li><svg width="10" height="9" viewBox="0 0 12 10"><rect x="0.5" y="0.5" width="11" height="9" fill="none" stroke="#aab4be"/><path d="M0.5 0.5L6 5.5L11.5 0.5" fill="none" stroke="#aab4be"/></svg>info@birchwoodstays.com</li>
      <li><svg width="10" height="12" viewBox="0 0 10 12"><path d="M5 11S1 6.5 1 4a4 4 0 0 1 8 0c0 2.5-4 7-4 7z" fill="#aab4be"/></svg>Birchwood Stays Ltd<br>12 Meadow Lane, Fernhill<br>Westshire FH4 2QT</li>
    </ul>
  </div>
  <div class="foot-col">
    <h5>Newsletter Signup</h5>
    <div class="field">Name</div>
    <div class="field">Email</div>
    <div class="btn">Submit</div>
  </div>
  <div class="foot-col" style="flex:1.6">
    <h5>Company Links</h5>
    <div class="links">
      <ul><li>About Us</li><li>News</li><li>Caravans &amp; Lodges</li><li>Late Deals</li><li>Holiday Parks</li><li>Gallery</li><li>Contact Us</li></ul>
      <ul><li>Frequent Questions</li><li>Local Attractions</li><li>Guest Reviews</li><li>Booking Terms</li><li>Privacy Policy</li><li>Site Map</li><li>Owners Area</li></ul>
    </div>
  </div>
</footer>
<div class="footer-bottom">
  <span>© 2013 Copyright · www.birchwoodstays.com</span>
  <div class="socials"><i></i><i></i><i></i><i></i></div>
</div>

</div>
</body>
</html>
```